Brevik Fabrication - Business Card Design

We would like a dark (likely black) themed business card to be able to hand out to potential clients. We may list our services on the card or keep it clean. Unsure. Logo attached

```html
<!DOCTYPE html>
<html lang="en">
<head>
<meta charset="UTF-8">
<title>Brevik Fabrication – Business Card</title>
<link href="https://fonts.googleapis.com/css2?family=Roboto:wght@400;500;900&display=swap" rel="stylesheet">
<style>
  :root {
    --bg: #cfd4d4;
    --card: #0e0e0f;
    --edge: #1f47c9;
    --red: #e2452b;
    --blue: #2b5ad8;
    --emboss: #3b3b3d;
  }
  * { box-sizing: border-box; margin: 0; padding: 0; }
  html, body { width: 1200px; height: 1200px; overflow: hidden; }
  body {
    background: var(--bg);
    font-family: "Roboto", Arial, sans-serif;
    position: relative;
  }
  .card {
    position: absolute;
    left: 240px;
    width: 720px;
    height: 410px;
    background: var(--card);
    border-bottom: 5px solid var(--edge);
    box-shadow: 0 18px 40px rgba(0,0,0,0.25);
  }
  .card--front { top: 150px; }
  .card--back { top: 640px; }

  .person { position: absolute; left: 50px; top: 70px; }
  .person__name {
    color: var(--red);
    font-size: 30px;
    font-weight: 400;
    letter-spacing: 0.5px;
    text-transform: uppercase;
    white-space: nowrap;
  }
  .person__role { color: var(--blue); font-size: 20px; margin-top: 4px; }

  .divider {
    position: absolute;
    left: 40px; right: 40px; top: 190px;
    height: 2px;
    background: var(--blue);
  }

  .contact { position: absolute; left: 50px; top: 215px; list-style: none; }
  .contact li {
    display: flex; align-items: center; gap: 12px;
    color: var(--blue); font-size: 20px; line-height: 34px;
  }
  .contact svg { width: 18px; height: 18px; flex: none; }

  .brand {
    position: absolute; right: 45px; top: 118px;
    display: flex; align-items: center; gap: 12px;
  }
  .brand__mark { width: 32px; height: 32px; border-radius: 50%; background: var(--red); flex: none; }
  .brand__name {
    color: var(--blue);
    font-size: 28px; font-weight: 900;
    text-transform: uppercase; letter-spacing: 0.5px;
    white-space: nowrap;
  }

  .address {
    position: absolute; right: 50px; bottom: 45px;
    text-align: right; color: var(--blue);
    font-size: 20px; line-height: 28px;
  }

  .card--back .brand {
    left: 0; right: 0; top: 0; bottom: 0;
    justify-content: center; gap: 18px;
  }
  .card--back .brand__mark { width: 52px; height: 52px; background: var(--emboss); }
  .card--back .brand__name { color: var(--emboss); font-size: 46px; }
</style>
</head>
<body>
  <section class="card card--front">
    <div class="person">
      <h1 class="person__name">Marcus Hale</h1>
      <p class="person__role">Manager</p>
    </div>

    <div class="brand">
      <span class="brand__mark"></span>
      <span class="brand__name">Brevik Fabrication</span>
    </div>

    <div class="divider"></div>

    <ul class="contact">
      <li>
        <svg viewBox="0 0 24 24" fill="none" stroke="#e2452b" stroke-width="2.2" stroke-linecap="round" stroke-linejoin="round"><path d="M5 3h4l2 5-2.5 1.5a11 11 0 0 0 6 6L16 13l5 2v4a2 2 0 0 1-2 2A16 16 0 0 1 3 5a2 2 0 0 1 2-2z"/></svg>
        555-018-7342
      </li>
      <li>
        <svg viewBox="0 0 24 24" fill="none" stroke="#e2452b" stroke-width="2.2" stroke-linejoin="round"><rect x="3" y="5" width="18" height="14" rx="1"/><path d="M3 6l9 7 9-7"/></svg>
        marcus@brevikfab.com
      </li>
      <li>
        <svg viewBox="0 0 24 24" fill="none" stroke="#e2452b" stroke-width="2"><circle cx="12" cy="12" r="9"/><path d="M3 12h18M12 3c3 3 3 15 0 18M12 3c-3 3-3 15 0 18"/></svg>
        www.brevikfab.com
      </li>
    </ul>

    <p class="address">Your address, city<br>state, ZIP 0000</p>
  </section>

  <section class="card card--back">
    <div class="brand">
      <span class="brand__mark"></span>
      <span class="brand__name">Brevik Fabrication</span>
    </div>
  </section>
</body>
</html>
```